Harbor Quill is a Smart Device and Wiring Business offering the latest in Smart Home Devices inc

Looking for a new website to draw people to my business and explain what a smart home is all about. I currently own a domain and have a website I put together in webnimbus business website builder. address www.harborquill.com. The website needs modernising and be visually appealing with cool action buttons, client feedback page etc.

The webpage needs to present an image of seamless integration of wireless voice control and smart devices that take tasks and activities away from the owner saving them time and money.

I have a chatterbay business page(harbor quill) and snapmeadow linked with the business, are we able to link this to the website somehow?

Target Market(s)

Residential home owners who want to modernise their home. Who have seen adverts for orbit nook and kestrel nova and want to put it in their home.

Industry/Entity Type

Technology Equipment

Number of Pages Required

1 page

Colors

Designer to choose colors to be used in the design.

Requirements
Must have
• A great landing page, that is modern and attractive, that gets across the idea of smart devices and technology.
• Must be ios/android device friendly.
Nice to have
• interactive/animated buttons
• I like the direction and interactiveness of these websites, a simplified version would be awesome.
• Something in between:
• http://www.oakridgelofts.com/ and https://plumcove.com/
• http://www.oakridgelofts.com/

```html
<!DOCTYPE html>
<html lang="en">
<head>
<meta charset="utf-8">
<title>Harbor Quill — Smart Device Integration</title>
<link href="https://fonts.googleapis.com/css2?family=Alegreya+Sans:wght@300;400;500;700&family=Open+Sans:wght@400;600;700&display=swap" rel="stylesheet">
<style>
:root{
  --blue:#2b72b6;
  --blue-dark:#1f5d98;
  --topbar:#2a6cae;
  --ink:#3a3a3a;
  --muted:#6d6d6d;
  --line:#cfd6de;
  --dark:#262729;
  --dark-2:#3a3b3e;
  --white:#ffffff;
  --field:#f7f7f7;
}
*{box-sizing:border-box;margin:0;padding:0}
html,body{width:1200px;height:3429px;overflow:hidden}
body{position:relative;font-family:"Open Sans",sans-serif;color:var(--ink);background:var(--white)}
.abs{position:absolute}
.accent{color:var(--blue)}
.btn{position:absolute;display:flex;align-items:center;justify-content:center;background:var(--blue);color:var(--white);border-radius:30px;font-size:13px;font-weight:700;letter-spacing:.3px;text-transform:uppercase}

/* top bar */
.topbar{top:0;left:0;width:1200px;height:50px;background:var(--topbar);color:var(--white);font-size:14px}
.topbar .social{position:absolute;left:80px;top:16px;font-size:12px;letter-spacing:.5px}
.topbar .contact-item{position:absolute;top:15px;display:flex;align-items:center;gap:10px}

/* header */
.site-header{top:50px;left:0;width:1200px;height:106px;background:var(--white);box-shadow:0 2px 6px rgba(0,0,0,.08)}
.brand{position:absolute;left:80px;top:28px;display:flex;align-items:center;gap:14px}
.brand .mark{width:50px;height:50px;border-radius:50%;background:var(--blue)}
.brand .name{font-family:"Alegreya Sans",sans-serif;font-weight:700;font-size:40px;color:#1d2b3a;letter-spacing:1px}
.nav a{position:absolute;top:43px;font-size:14px;color:#4a4a4a;text-decoration:none}
.nav a.active{color:var(--blue)}

/* hero */
.hero{top:156px;left:0;width:1200px;height:575px;background:linear-gradient(120deg,#3a3b3e 0%,#1f2022 45%,#333437 70%,#1c1d1f 100%)}
.hero .product-visual{position:absolute;left:80px;top:15px;width:503px;height:526px;border-radius:16px;background:radial-gradient(ellipse at 45% 45%,#5a5d62 0%,#2f3134 60%,rgba(40,41,44,0) 100%)}
.hero h1{position:absolute;left:663px;top:144px;color:var(--white);font-family:"Alegreya Sans",sans-serif;font-weight:500;font-size:60px;line-height:1.02;letter-spacing:.5px}
.hero p{position:absolute;left:663px;top:290px;width:440px;color:#e8e8e8;font-size:15.5px;line-height:26px}

/* section titles */
.section-title{position:absolute;left:0;width:1200px;text-align:center;font-family:"Alegreya Sans",sans-serif;font-weight:400;font-size:40px;color:#4a4a4a}

/* what we do */
.what-we-do .lead{position:absolute;left:279px;top:862px;width:642px;text-align:center;font-size:14px;line-height:25px;color:var(--muted)}
.process-line{position:absolute;top:1076px;height:2px;background:var(--line)}
.process-node{position:absolute;top:1066px;width:22px;height:22px;border-radius:50%;border:2px solid var(--line);background:var(--white)}
.step{position:absolute;top:1054px;width:270px;text-align:center}
.step svg{display:block;margin:0 auto}
.step h3{margin-top:16px;font-size:15px;font-weight:400;color:var(--ink)}
.step h3.accent{color:var(--blue)}
.step p{margin-top:8px;font-size:13px;line-height:23px;color:var(--muted)}
.read-more{color:var(--blue);text-decoration:underline}

/* welcome */
.welcome{top:1271px;left:0;width:1200px;height:459px;background:linear-gradient(90deg,#1e1f21 0%,#2d2e31 55%,#4a4b4f 100%)}
.welcome h2{position:absolute;left:80px;top:60px;color:var(--white);font-family:"Alegreya Sans",sans-serif;font-weight:400;font-size:40px}
.welcome p{position:absolute;left:80px;top:130px;width:585px;color:#f0f0f0;font-size:14.5px;line-height:26px}
.welcome .feature-circle{position:absolute;left:740px;top:57px;width:284px;height:284px;border-radius:50%;border:5px solid var(--blue);background:radial-gradient(circle at 50% 45%,#6d86a8 0%,#3d4f67 60%,#23303f 100%)}

/* specialists */
.card{position:absolute;top:1877px;width:322px}
.card .photo{width:322px;height:205px;border-bottom:5px solid var(--blue)}
.card h3{margin-top:24px;text-align:center;font-size:16px;font-weight:600;color:var(--blue)}
.card p{margin-top:8px;text-align:center;font-size:13px;line-height:23px;color:var(--muted)}
.slider-arrow{position:absolute;top:2010px;width:41px;height:31px;background:var(--blue)}

/* products */
.products{top:2252px;left:0;width:1200px;height:372px;background:linear-gradient(90deg,#1e1f21 0%,#2c2d30 50%,#3b3c40 100%)}
.products h2{position:absolute;left:80px;top:60px;color:var(--white);font-family:"Alegreya Sans",sans-serif;font-weight:400;font-size:40px}
.products .intro{position:absolute;left:80px;top:130px;width:410px;color:#f0f0f0;font-size:13.5px;line-height:25px}
.package{position:absolute;top:113px;width:210px;text-align:center}
.package .badge{width:104px;height:104px;margin:0 auto;border-radius:50%;background:var(--white);border:5px solid var(--blue);box-shadow:0 0 0 3px rgba(255,255,255,.5);display:flex;align-items:center;justify-content:center;color:var(--blue);font-size:14px;line-height:20px}
.package p{margin-top:22px;color:#f0f0f0;font-size:13px;line-height:25px}

/* contact */
.contact h2{position:absolute;left:80px;top:2688px;font-family:"Alegreya Sans",sans-serif;font-weight:400;font-size:40px;color:#4a4a4a}
.field{position:absolute;background:var(--field);border:1px solid #d9d9d9;border-radius:26px;font-size:13px;color:#555;padding:14px 0 0 12px}
.submit{position:absolute;left:78px;top:3001px;width:653px;height:51px;border-radius:26px;background:var(--blue);color:var(--white);font-size:13px;font-weight:700;display:flex;align-items:center;justify-content:center}
.info-item{position:absolute;left:800px;display:flex;gap:22px;font-size:13.5px;line-height:25px;color:var(--muted)}
.info-item svg{flex:none;margin-top:4px}

/* footer */
.site-footer{top:3113px;left:0;width:1200px;height:316px;background:linear-gradient(90deg,#141416 0%,#1f2022 60%,#2d2e31 100%);color:var(--white)}
.site-footer .brand{left:0;width:1200px;top:45px;justify-content:center}
.site-footer .brand .mark{background:var(--white)}
.site-footer .brand .name{color:var(--white)}
.footer-nav{position:absolute;top:140px;left:0;width:1200px;text-align:center;font-size:14px}
.footer-nav span{margin:0 18px}
.footer-social{position:absolute;top:195px;left:0;width:1200px;text-align:center;font-size:13px;letter-spacing:.5px}
.footer-rule{position:absolute;top:252px;left:78px;width:1044px;height:1px;background:rgba(255,255,255,.55)}
.copyright{position:absolute;top:274px;left:0;width:1200px;text-align:center;font-size:13px}
</style>
</head>
<body>

<div class="abs topbar">
  <div class="social">chatterbay &nbsp;·&nbsp; snapmeadow &nbsp;·&nbsp; chirplane</div>
  <div class="contact-item" style="left:720px">
    <svg width="16" height="16" viewBox="0 0 24 24"><path fill="#fff" d="M6.6 10.8a15.1 15.1 0 0 0 6.6 6.6l2.2-2.2c.3-.3.7-.4 1-.2 1.1.4 2.3.6 3.6.6.6 0 1 .4 1 1V20c0 .6-.4 1-1 1A17 17 0 0 1 3 4c0-.6.4-1 1-1h3.5c.6 0 1 .4 1 1 0 1.3.2 2.5.6 3.6.1.3 0 .7-.2 1z"/></svg>
    <span>0400 318 562</span>
  </div>
  <div class="contact-item" style="left:891px">
    <svg width="16" height="12" viewBox="0 0 16 12"><rect width="16" height="12" rx="1" fill="#fff"/><path d="M1 1l7 5 7-5" stroke="#2a6cae" stroke-width="1.4" fill="none"/></svg>
    <span>info@harborquill.com.au</span>
  </div>
</div>

<header class="abs site-header">
  <div class="brand"><span class="mark"></span><span class="name">Harbor Quill</span></div>
  <nav class="nav">
    <a class="active" style="left:503px">Home</a>
    <a style="left:599px">About Us</a>
    <a style="left:718px">What We Do</a>
    <a style="left:862px">Products</a>
    <a style="left:981px">Contact Us</a>
  </nav>
  <svg class="abs" style="left:1098px;top:40px" width="22" height="22" viewBox="0 0 22 22"><circle cx="9" cy="9" r="6.5" stroke="#2b72b6" stroke-width="2.4" fill="none"/><path d="M14 14l6 6" stroke="#2b72b6" stroke-width="2.6" stroke-linecap="round"/></svg>
</header>

<section class="abs hero">
  <div class="product-visual" role="img" aria-label="Group of smart speakers and voice assistant devices"></div>
  <h1>SMART DEVICE<br>INTEGRATION</h1>
  <p>We are focused on delivering affordable and easily usable devices for your home and office</p>
  <div class="btn" style="left:663px;top:365px;width:153px;height:53px">Request Quote</div>
</section>

<section class="what-we-do">
  <h2 class="section-title" style="top:790px">What <span class="accent">We Do</span></h2>
  <p class="lead">We are a small group of Perth Tech consultants, with long-term experience in the integration, setup and fault finding of advanced technologies, we are passionate about the products we sell and confident in the service we provide.</p>
  <div class="btn" style="left:533px;top:969px;width:134px;height:53px">Know More</div>

  <div class="process-line" style="left:238px;width:170px"></div>
  <div class="process-line" style="left:505px;width:185px"></div>
  <div class="process-line" style="left:775px;width:190px"></div>
  <div class="process-node" style="left:316px;border-color:var(--blue)"><svg width="18" height="18" viewBox="0 0 18 18"><path d="M4.5 9.5l3 3 6-6.5" stroke="#2b72b6" stroke-width="1.8" fill="none"/></svg></div>
  <div class="process-node" style="left:588px"></div>
  <div class="process-node" style="left:865px"></div>

  <div class="step" style="left:62px">
    <svg width="52" height="48" viewBox="0 0 52 48"><rect x="2" y="2" width="34" height="26" rx="4" stroke="#2b72b6" stroke-width="3" fill="none"/><path d="M10 28v10l8-10" stroke="#2b72b6" stroke-width="3" fill="none"/><rect x="20" y="16" width="30" height="22" rx="4" fill="#2b72b6"/><path d="M42 38v8l-8-8" fill="#2b72b6"/></svg>
    <h3 class="accent">Consultation</h3>
    <p>We meet to discuss your vision,<br>gather...<span class="read-more">Read More</span></p>
  </div>
  <div class="step" style="left:329px">
    <svg width="48" height="48" viewBox="0 0 48 48"><rect x="8" y="3" width="28" height="38" rx="3" stroke="#444" stroke-width="3" fill="none"/><path d="M14 14h16M14 21h16M14 28h9" stroke="#444" stroke-width="2.5"/><circle cx="35" cy="35" r="9" fill="#fff" stroke="#444" stroke-width="3"/><path d="M31 35l3 3 5-6" stroke="#444" stroke-width="2.5" fill="none"/></svg>
    <h3>Installation</h3>
    <p>Upon acceptance of project<br>document we...<span class="read-more">Read More</span></p>
  </div>
  <div class="step" style="left:599px">
    <svg width="48" height="48" viewBox="0 0 48 48"><path d="M4 30l6-14h28l6 14v12H4z" fill="#444"/><path d="M24 4v18M17 15l7 7 7-7" stroke="#fff" stroke-width="3" fill="none"/><path d="M4 30h12l3 5h10l3-5h12" stroke="#fff" stroke-width="2" fill="none"/></svg>
    <h3>Finalisation</h3>
    <p>After installing the product we<br>run you...<span class="read-more">Read More</span></p>
  </div>
  <div class="step" style="left:871px">
    <svg width="48" height="48" viewBox="0 0 48 48"><circle cx="24" cy="16" r="10" fill="#444"/><path d="M6 46c0-11 8-17 18-17s18 6 18 17z" fill="#444"/><path d="M12 18a12 12 0 0 1 24 0" stroke="#444" stroke-width="2.5" fill="none"/></svg>
    <h3>Support</h3>
    <p>We offer tech support when<br>difficulties arise,...<span class="read-more">Read More</span></p>
  </div>
</section>

<section class="abs welcome">
  <h2>Welcome To Harbor Quill</h2>
  <p>Lorem Ipsum is simply dummy text of the printing and typesetting industry. Lorem Ipsum has been the industry's standard dummy text ever when an unknown printer took a galley of type and scrambled it to make a type specimen book. It has survived not only five centuries, but also the leap into typesetting, remaining essentially unchanged. It was popularised in the 1960s with the release of Typeleaf sheets containing Lorem Ipsum passages, and with desktop publishing software like Pressdeck Layout including versions of Lorem Ipsum.</p>
  <div class="btn" style="left:80px;top:343px;width:137px;height:57px">Know More</div>
  <div class="feature-circle" role="img" aria-label="Hands holding a tablet showing a home control screen"></div>
</section>

<section class="specialists">
  <h2 class="section-title" style="top:1790px">Smart <span class="accent">Home Specialists</span></h2>
  <div class="slider-arrow" style="left:18px"><svg width="41" height="31" viewBox="0 0 41 31"><path d="M21 10l-6 5.5 6 5.5M28 10l-6 5.5 6 5.5" stroke="#fff" stroke-width="2.2" fill="none"/></svg></div>
  <div class="slider-arrow" style="left:1141px"><svg width="41" height="31" viewBox="0 0 41 31"><path d="M13 10l6 5.5-6 5.5M20 10l6 5.5-6 5.5" stroke="#fff" stroke-width="2.2" fill="none"/></svg></div>

  <div class="card" style="left:78px">
    <div class="photo" role="img" aria-label="Living room with a hand holding a remote control" style="background:linear-gradient(135deg,#d9d3c8,#8f8a82 60%,#5b5954)"></div>
    <h3>Home Automation</h3>
    <p>Your own concierge in a box, control your<br>home devices, lights and...<span class="read-more">Read More</span></p>
  </div>
  <div class="card" style="left:439px">
    <div class="photo" role="img" aria-label="Smart speaker on a kitchen bench" style="background:linear-gradient(135deg,#bfc6cc,#7d848b 55%,#4f555b)"></div>
    <h3>Voice Control With Kestrel Nova</h3>
    <p>Your own concierge in a box, control your<br>home devices, lights and...<span class="read-more">Read More</span></p>
  </div>
  <div class="card" style="left:800px">
    <div class="photo" role="img" aria-label="Phone app unlocking a smart door lock" style="background:linear-gradient(135deg,#4a4a4c,#2c2c2e 55%,#8b7a5e)"></div>
    <h3>Keyless Entry</h3>
    <p>Your own concierge in a box, control your<br>home devices, lights and...<span class="read-more">Read More</span></p>
  </div>
</section>

<section class="abs products">
  <h2>Our Products</h2>
  <p class="intro">Lorem Ipsum is simply dummy text of the printing and typesetting industry. Lorem Ipsum has been the industry's standard dummy text ever since the 1500s, when an unknown printer took a galley of type and scrambled it to make a type specimen book. It has survived not only five centuries, but also the leap into electronic typesetting, remaining essentially unchanged.</p>
  <div class="package" style="left:528px">
    <div class="badge">Silver<br>Package</div>
    <p>The Silver Package gives<br>you the foundation of a<br>Smart...<span class="read-more">Read More</span></p>
  </div>
  <div class="package" style="left:727px">
    <div class="badge">Gold<br>Package</div>
    <p>The Gold package takes<br>the foundation of the<br>Silver...<span class="read-more">Read More</span></p>
  </div>
  <div class="package" style="left:926px">
    <div class="badge">Platinum<br>Package</div>
    <p>The Platinum Package has<br>all the bells and<br>whistles...<span class="read-more">Read More</span></p>
  </div>
</section>

<section class="contact">
  <h2>Contact <span class="accent">Us</span></h2>
  <div class="field" style="left:78px;top:2761px;width:320px;height:53px">Name*</div>
  <div class="field" style="left:411px;top:2761px;width:320px;height:53px">E-mail*</div>
  <div class="field" style="left:78px;top:2825px;width:320px;height:53px">Phone*</div>
  <div class="field" style="left:411px;top:2825px;width:320px;height:53px">Subject</div>
  <div class="field" style="left:78px;top:2887px;width:653px;height:101px">Message</div>
  <div class="submit">SUBMIT</div>

  <div class="info-item" style="top:2832px">
    <svg width="14" height="18" viewBox="0 0 14 18"><path d="M7 0a7 7 0 0 1 7 7c0 5-7 11-7 11S0 12 0 7a7 7 0 0 1 7-7z" fill="#2b72b6"/><circle cx="7" cy="7" r="2.6" fill="#fff"/></svg>
    <span>123,Lorem Ipsum is simply<br>dummy text of the printing</span>
  </div>
  <div class="info-item" style="top:2912px">
    <svg width="14" height="14" viewBox="0 0 24 24"><path fill="#2b72b6" d="M6.6 10.8a15.1 15.1 0 0 0 6.6 6.6l2.2-2.2c.3-.3.7-.4 1-.2 1.1.4 2.3.6 3.6.6.6 0 1 .4 1 1V20c0 .6-.4 1-1 1A17 17 0 0 1 3 4c0-.6.4-1 1-1h3.5c.6 0 1 .4 1 1 0 1.3.2 2.5.6 3.6.1.3 0 .7-.2 1z"/></svg>
    <span>0400 318 562</span>
  </div>
  <div class="info-item" style="top:2962px">
    <svg width="14" height="11" viewBox="0 0 16 12"><rect width="16" height="12" rx="1" fill="#2b72b6"/><path d="M1 1l7 5 7-5" stroke="#fff" stroke-width="1.4" fill="none"/></svg>
    <span>info@harborquill.com.au</span>
  </div>
</section>

<footer class="abs site-footer">
  <div class="brand"><span class="mark"></span><span class="name">Harbor Quill</span></div>
  <div class="footer-nav"><span>Home</span>|<span>About Us</span>|<span>What We Do</span>|<span>Products</span>|<span>Contact Us</span></div>
  <div class="footer-social">chatterbay &nbsp;·&nbsp; snapmeadow &nbsp;·&nbsp; chirplane</div>
  <div class="footer-rule"></div>
  <div class="copyright">© HARBOR QUILL - 2018. All Rights Reserved.</div>
</footer>

</body>
</html>
```